High-End Medical Center Website Design Project

This design is part of a well thought-out project by an experienced project manager / developer. The approved wireframe is attached. Creative interpretations / suggestions based on the layout encouraged.

The design is for a new state-of-the-art medical center located in Dallas, Texas. The target audience would likely be individuals (approx. 60% female /40% male) who are the healthcare decision-makers for their families. They would likely have insurance and be inclined to seek out top-quality care.

Potential clients would choose this client over others in their industry because the medical center is physician owned, meaning it is patient-focused rather than profit-focused. The facility is brand new, featuring the latest technology. (This includes an amazing waiting room featuring WiFi and docking stations.) The physicians are hand-picked by referral only.

The look of the site should be extremely clean. We are going for a well-organized, professional look with a bit of a warm glow (interpret that however you like). Use crisp corners and the colors in the logo.

Think modern, clean with some great use of color / font.

We can get lovely photography of the medical center once construction is complete. Feel free to use an "example image" behind the Featured Area ("Physician Owned. Patient-Focused") if you like. We are open to ideas.

ONE CHANGE REQUESTED IN THE WIREFRAME:

Remove the "Connect" 1/4 page footer area and replace with a quick contact form. You may swap the "Locations" area with the form if desired. Put social media icons at the top left of the page in the top header area.

(Note: Please use social media icons that match the design rather than standard icons. We preferred not placing the icons at the top, but the client requested this. Let's not bring more attention to them than necessary.)
Updates

We're custom programming this site, so there's no need to base it on a template. Also, we would prefer not to use typical "seen everywhere" stock images.Thanks.

Industry/Entity Type

Construction

Requirements
Must have
• Follow the wireframe. This has been approved.
Nice to have
• Examples of what hover states, links or dropdowns might look like.

```html
<!DOCTYPE html>
<html lang="en">
<head>
<meta charset="utf-8">
<title>Lumen Medical Center</title>
<link href="https://fonts.googleapis.com/css2?family=Open+Sans:wght@400;600;700&family=Roboto+Condensed:wght@300;400&family=Noto+Serif:ital@1&display=swap" rel="stylesheet">
<style>
:root{
  --blue:#0b5aa6;
  --blue-dark:#084a8a;
  --teal:#47adb9;
  --teal-dark:#15878f;
  --accent:#3a9fc0;
  --orange:#e05400;
  --ink:#222;
  --grey:#8a8a8a;
  --card:#f4f4f4;
  --line:#dedede;
  --white:#fff;
}
*{box-sizing:border-box;margin:0;padding:0}
html,body{width:813px;height:1200px;overflow:hidden;background:var(--white)}
body{position:relative;font-family:"Open Sans",Arial,sans-serif;color:var(--ink)}
.abs{position:absolute}
.topbar{left:0;top:0;width:813px;height:20px;background:linear-gradient(#f4f4f4,#e2e2e2);border-bottom:1px solid #d6d6d6}
.social-dot{position:absolute;width:12px;height:12px;border-radius:50%;background:#c9ccd0}
.topbar .social-dot:first-child{background:var(--blue)}
.topbar-phone{right:88px;top:3px;font-size:10px;font-weight:700;color:#555}
.header{left:0;top:20px;width:813px;height:53px;background:var(--white)}
.brand{left:88px;top:35px;display:flex;align-items:center;gap:8px}
.brand-square{width:22px;height:22px;background:var(--blue)}
.brand-name{font-size:17px;font-weight:700;color:var(--blue);letter-spacing:.2px}
.nav{left:358px;top:20px;height:53px;display:flex}
.nav-item{height:53px;display:flex;flex-direction:column;align-items:center;justify-content:flex-end;padding-bottom:6px;font-size:8.5px;font-weight:700;color:#666;text-align:center}
.nav-item svg{margin-bottom:5px}
.nav-item.is-active{background:var(--blue);color:var(--white);position:relative}
.nav-item.is-active::after{content:"";position:absolute;bottom:-5px;left:50%;margin-left:-5px;border:5px solid transparent;border-bottom:0;border-top-color:var(--blue)}
.hero{left:0;top:73px;width:813px;height:313px;background:linear-gradient(180deg,#9fb4a6 0%,#c8cfca 35%,#7d8d6c 70%,#505b44 100%)}
.hero-band{left:0;top:335px;width:813px;height:51px;background:rgba(40,45,50,.45)}
.hero-title{left:0;top:92px;width:813px;text-align:center;font-size:23px;font-weight:700;color:var(--white);text-shadow:0 1px 3px rgba(0,0,0,.35)}
.hex{position:absolute;top:296px;width:72px;height:80px}
.section-title{left:0;top:406px;width:813px;text-align:center;font-family:"Roboto Condensed",sans-serif;font-weight:300;font-size:22px;color:#222}
.rule{height:1px;background:var(--line);top:421px}
.rule-dot{width:6px;height:6px;border-radius:50%;background:#cfcfcf;top:418px}
.feature{top:471px;width:190px;height:158px;background:var(--card);border:1px solid var(--line);text-align:center;padding-top:31px}
.feature h3{font-size:11.5px;font-weight:600;color:#222}
.feature .sub{font-size:8.5px;color:var(--orange);margin-top:2px}
.feature p{font-size:8.5px;line-height:12.6px;color:#333;margin:10px 16px 0}
.btn-more{display:inline-flex;margin-top:12px;font-size:7px;color:#666;background:#e2e2e2}
.btn-more span{padding:2px 6px}
.btn-more b{padding:2px 5px;background:#d5d5d5;font-weight:400}
.pin{position:absolute;top:447px;width:40px;height:50px}
.divider{left:88px;top:653px;width:637px;height:7px;background:#f0f0f0}
.photo-frame{left:88px;top:685px;width:124px;height:134px;border:1px solid #e3e3e3;padding:6px;background:#fafafa}
.photo-fill{width:100%;height:100%;background:linear-gradient(160deg,#e8eef0,#c9d6dc 60%,#9fb3bd)}
.h-light{font-family:"Roboto Condensed",sans-serif;font-weight:300;font-size:22px;white-space:nowrap}
.about-title{left:230px;top:682px;color:var(--accent)}
.about-text{left:230px;top:714px;width:275px;font-size:8.5px;line-height:12.7px;color:#222}
.about-text p+p{margin-top:12px}
.link{color:var(--accent);font-size:8.5px}
.testi-title{left:535px;top:682px;color:#1d6aa6}
.testi-text{left:560px;top:715px;width:166px;font-family:"Noto Serif",Georgia,serif;font-style:italic;font-size:8.5px;line-height:12.6px;color:#333}
.testi-text p+p{margin-top:12px}
.testi-author{font-family:"Open Sans",sans-serif;font-style:normal;font-weight:700;color:var(--blue);margin-top:12px;font-size:8px}
.footer{left:0;top:903px;width:813px;height:205px;background:var(--teal)}
.foot-title{font-family:"Roboto Condensed",sans-serif;font-weight:300;font-size:18px;color:var(--white);top:918px}
.news-list{top:955px;width:130px;list-style:none;font-size:8.5px;color:var(--white)}
.news-list li{padding-left:10px;position:relative;margin-bottom:9px;line-height:12.5px}
.news-list li::before{content:"";position:absolute;left:1px;top:5px;border:3px solid transparent;border-left:4px solid var(--white);border-right:0}
.news-list .date{font-size:8px;display:block;margin-left:-1px}
.loc-row{left:405px;width:150px;display:flex;gap:14px;font-size:8.5px;color:var(--white);line-height:12.5px}
.loc-icon{width:18px;height:18px;border-radius:50%;background:var(--teal-dark);flex:none;display:flex;align-items:center;justify-content:center}
.contact-panel{left:565px;top:893px;width:160px;height:288px}
.contact-title{left:586px;top:918px;font-family:"Roboto Condensed",sans-serif;font-weight:300;font-size:18px;color:var(--white)}
.field{left:586px;width:125px;height:19px;background:var(--white);border:1px solid #cfe3e5;font-family:"Noto Serif",Georgia,serif;font-style:italic;font-size:8px;color:#333;padding:3px 6px}
.submit{left:587px;top:1071px;font-size:13px;font-weight:700;color:var(--white)}
.copyright{left:572px;top:1108px;width:153px;text-align:center;font-size:8px;color:var(--white)}
.newsletter{left:0;top:1108px;width:572px;height:34px;background:var(--blue)}
.news-label{left:88px;top:1115px;width:140px;font-family:"Roboto Condensed",sans-serif;font-weight:300;font-size:15.5px;letter-spacing:-.3px;white-space:nowrap;color:var(--white)}
.news-field{top:1116px;width:124px;height:20px;background:var(--white);border-radius:2px;font-family:"Noto Serif",Georgia,serif;font-style:italic;font-size:8px;padding:5px 7px;color:#333}
</style>
</head>
<body>

<div class="abs topbar">
  <span class="social-dot" style="left:89px;top:3px"></span>
  <span class="social-dot" style="left:108px;top:3px"></span>
  <span class="social-dot" style="left:127px;top:3px"></span>
</div>
<div class="abs topbar-phone">&#9646; (555) 014-2290</div>

<header class="abs header"></header>
<div class="abs brand"><span class="brand-square"></span><span class="brand-name">LUMEN MEDICAL CENTER</span></div>

<nav class="abs nav">
  <a class="nav-item is-active" style="width:59px">
    <svg width="18" height="18" viewBox="0 0 20 20"><path d="M10 1l2.6 6 6.4.5-4.9 4.2 1.5 6.3L10 14.7 4.4 18l1.5-6.3L1 7.5 7.4 7z" fill="#fff"/></svg>Why Lumen</a>
  <a class="nav-item" style="width:72px">
    <svg width="20" height="18" viewBox="0 0 20 18"><circle cx="12" cy="5" r="4" fill="#b5b5b5"/><path d="M4 18c0-5 3-7 8-7s7 2 7 7z" fill="#b5b5b5"/><circle cx="5" cy="7" r="3" fill="none" stroke="#b5b5b5" stroke-width="1.5"/></svg>Physicians</a>
  <a class="nav-item" style="width:72px">
    <svg width="14" height="20" viewBox="0 0 14 20"><path d="M7 1a6 6 0 0 0-4 10.5V15h8v-3.5A6 6 0 0 0 7 1z" fill="none" stroke="#b5b5b5" stroke-width="1.6"/><rect x="4" y="16" width="6" height="3" fill="#b5b5b5"/></svg>Specialities</a>
  <a class="nav-item" style="width:44px">
    <svg width="8" height="20" viewBox="0 0 8 20"><circle cx="5" cy="2.5" r="2.2" fill="#b5b5b5"/><path d="M2 7h4l-2 11h-3z" fill="#b5b5b5"/></svg>Info</a>
  <a class="nav-item" style="width:64px">
    <svg width="20" height="18" viewBox="0 0 20 18"><path d="M1 17l4-8 4 4 3-7 7 11z" fill="#b5b5b5"/><circle cx="10" cy="4" r="3" fill="#b5b5b5"/></svg>Locations</a>
  <a class="nav-item" style="width:60px">
    <svg width="20" height="16" viewBox="0 0 20 16"><rect x="1" y="2" width="18" height="13" rx="1" fill="none" stroke="#b5b5b5" stroke-width="1.6"/><rect x="4" y="5" width="5" height="6" fill="#b5b5b5"/><path d="M11 6h5M11 9h5" stroke="#b5b5b5" stroke-width="1.4"/></svg>Contact</a>
</nav>

<div class="abs hero" role="img" aria-label="Photo of four smiling physicians in front of the medical center building with palm trees"></div>
<div class="abs hero-band"></div>
<h1 class="abs hero-title">Physician Owned. Patient-Focused</h1>

<svg class="hex" style="left:205px" viewBox="0 0 72 80"><polygon points="36,2 70,21 70,59 36,78 2,59 2,21" fill="#e9edf0"/><polygon points="36,8 65,24 65,56 36,72 7,56 7,24" fill="#fff"/>
  <path d="M25 26v10a9 9 0 0 0 18 0V26M34 45v6a8 8 0 0 0 16 0v-3" fill="none" stroke="#2e9cb7" stroke-width="3"/><circle cx="50" cy="45" r="4" fill="none" stroke="#2e9cb7" stroke-width="3"/></svg>
<svg class="hex" style="left:370px" viewBox="0 0 72 80"><polygon points="36,2 70,21 70,59 36,78 2,59 2,21" fill="#e9edf0"/><polygon points="36,8 65,24 65,56 36,72 7,56 7,24" fill="#fff"/>
  <path d="M19 28h12l3 4h19v20H19z" fill="none" stroke="#2e9cb7" stroke-width="3" stroke-linejoin="round"/><path d="M19 36h34" stroke="#2e9cb7" stroke-width="2"/></svg>
<svg class="hex" style="left:535px" viewBox="0 0 72 80"><polygon points="36,2 70,21 70,59 36,78 2,59 2,21" fill="#e9edf0"/><polygon points="36,8 65,24 65,56 36,72 7,56 7,24" fill="#fff"/>
  <path d="M28 32a8 8 0 1 1 12 7c-3 2-4 3-4 7" fill="none" stroke="#2e9cb7" stroke-width="5"/><circle cx="36" cy="54" r="3" fill="#2e9cb7"/></svg>

<h2 class="abs section-title">What Sets Us Apart</h2>
<div class="abs rule" style="left:88px;width:212px"></div>
<div class="abs rule-dot" style="left:298px"></div>
<div class="abs rule-dot" style="left:509px"></div>
<div class="abs rule" style="left:513px;width:212px"></div>

<article class="abs feature" style="left:89px"><h3>Technology</h3><div class="sub">Neque porro quisquam est qui</div><p>Lorem Ipsum is simply dummy text of the printing and typesetting industry. Lorem Ipsum has been the industry's standard dummy text..</p><span class="btn-more"><span>Read more</span><b>+</b></span></article>
<article class="abs feature" style="left:312px"><h3>Quality of Care</h3><div class="sub">Neque porro quisquam est qui</div><p>Lorem Ipsum is simply dummy text of the printing and typesetting industry. Lorem Ipsum has been the industry's standard dummy text..</p><span class="btn-more"><span>Read more</span><b>+</b></span></article>
<article class="abs feature" style="left:535px"><h3>Patient Experience</h3><div class="sub">Neque porro quisquam est qui</div><p>Lorem Ipsum is simply dummy text of the printing and typesetting industry. Lorem Ipsum has been the industry's standard dummy text..</p><span class="btn-more"><span>Read more</span><b>+</b></span></article>

<svg class="pin" style="left:164px" viewBox="0 0 40 50"><path d="M20 1a19 19 0 0 1 6 37l-6 10-6-10A19 19 0 0 1 20 1z" fill="var(--blue)"/><path d="M20 29l-8-8a4.5 4.5 0 0 1 8-5 4.5 4.5 0 0 1 8 5z" fill="none" stroke="#fff" stroke-width="2"/></svg>
<svg class="pin" style="left:387px" viewBox="0 0 40 50"><path d="M20 1a19 19 0 0 1 6 37l-6 10-6-10A19 19 0 0 1 20 1z" fill="var(--blue)"/><path d="M12 19h4v10h-4zM17 19l4-8c2 0 2 2 2 3l-1 4h6c1 0 2 1 1 3l-2 7c0 1-1 1-2 1h-8z" fill="#fff"/></svg>
<svg class="pin" style="left:610px" viewBox="0 0 40 50"><path d="M20 1a19 19 0 0 1 6 37l-6 10-6-10A19 19 0 0 1 20 1z" fill="var(--blue)"/><circle cx="20" cy="19" r="9" fill="none" stroke="#fff" stroke-width="2"/><circle cx="17" cy="17" r="1.3" fill="#fff"/><circle cx="23" cy="17" r="1.3" fill="#fff"/><path d="M15.5 21a5 5 0 0 0 9 0" fill="none" stroke="#fff" stroke-width="1.6"/></svg>

<div class="abs divider"></div>

<div class="abs photo-frame"><div class="photo-fill" role="img" aria-label="Photo of three physicians in white coats with stethoscopes"></div></div>
<h2 class="abs h-light about-title">Heading Here</h2>
<div class="abs about-text">
  <p>Lorem Ipsum is simply dummy text of the printing and typesetting industry. Lorem Ipsum has been the industry's standard dummy text ever since the 1500s.</p>
  <p>When an unknown printer took a galley of type and scrambled it to make a type specimen book.</p>
  <p><a class="link">Read more...</a></p>
</div>

<h2 class="abs h-light testi-title">Testimonials</h2>
<svg class="abs" style="left:535px;top:718px" width="16" height="16" viewBox="0 0 16 16"><path d="M4 1h11v8H8l-3 3V9H4z" fill="#b0b0b0"/><path d="M1 5h2v6h2v3l3-3h4v2H8l-4 3v-3H1z" fill="#c8c8c8"/></svg>
<div class="abs testi-text">
  <p>Lorem Ipsum is simply dummy text of the printing and typesetting industry. Lorem Ipsum has been the industry's standard dummy text ever since the 1500s.</p>
  <p>When an unknown printer took a galley of type and scrambled it to make a type specimen book.</p>
  <p class="testi-author">- Maria Delgado</p>
</div>

<footer class="abs footer"></footer>
<h3 class="abs foot-title" style="left:88px">News</h3>
<ul class="abs news-list" style="left:88px">
  <li><span class="date">July, 24 2013</span>Neque porro quisquam est qui dolorem ipsum</li>
  <li><span class="date">July, 24 2013</span>Neque porro quisquam est qui dolorem ipsum</li>
  <li><span class="date">July, 24 2013</span>Neque porro quisquam est qui dolorem ipsum</li>
</ul>
<h3 class="abs foot-title" style="left:251px">Blog</h3>
<ul class="abs news-list" style="left:251px">
  <li><span class="date">July, 24 2013</span>Neque porro quisquam est qui dolorem ipsum</li>
  <li><span class="date">July, 24 2013</span>Neque porro quisquam est qui dolorem ipsum</li>
  <li><span class="date">July, 24 2013</span>Neque porro quisquam est qui dolorem ipsum</li>
</ul>
<h3 class="abs foot-title" style="left:405px">Location</h3>
<div class="abs loc-row" style="top:956px"><span class="loc-icon"><svg width="8" height="10" viewBox="0 0 8 10"><path d="M4 0a4 4 0 0 1 4 4c0 3-4 6-4 6S0 7 0 4a4 4 0 0 1 4-4z" fill="#fff"/></svg></span><div>Address:<br>Neque porro quisquam est qui dolorem ipsum</div></div>
<div class="abs loc-row" style="top:1002px"><span class="loc-icon"><svg width="9" height="9" viewBox="0 0 10 10"><path d="M1 1l3-1 1 3-1.5 1a6 6 0 0 0 2.5 2.5L7 5l3 1-1 3C4 9 1 6 1 1z" fill="#fff"/></svg></span><div>Phone:<br>555 014 22907</div></div>
<div class="abs loc-row" style="top:1034px"><span class="loc-icon"><svg width="10" height="7" viewBox="0 0 10 7"><rect width="10" height="7" fill="#fff"/><path d="M0 0l5 4 5-4" fill="none" stroke="#15878f"/></svg></span><div>Email:<br>hello@lumenclinic.test</div></div>

<svg class="abs contact-panel" viewBox="0 0 160 288"><path d="M7 0L0 8h7z" fill="#0e6a70"/><path d="M7 0h153v268l-76 20-77-20z" fill="var(--teal-dark)"/></svg>
<h3 class="abs contact-title">Contact</h3>
<div class="abs field" style="top:952px">Name:</div>
<div class="abs field" style="top:978px">Email:</div>
<div class="abs field" style="top:1003px">Phone:</div>
<div class="abs field" style="top:1028px;height:36px">Message:</div>
<div class="abs submit">Submit »</div>
<div class="abs copyright">©2013 Lumen Medical Center</div>
<span class="abs social-dot" style="left:624px;top:1130px;background:#5fb3b8"></span>
<span class="abs social-dot" style="left:642px;top:1130px;background:#5fb3b8"></span>
<span class="abs social-dot" style="left:660px;top:1130px;background:#5fb3b8"></span>

<div class="abs newsletter"></div>
<div class="abs news-label">Newsletter Subscribe:</div>
<div class="abs news-field" style="left:236px">Enter Name:</div>
<div class="abs news-field" style="left:365px">Enter Email:</div>
<svg class="abs" style="left:496px;top:1118px" width="14" height="14" viewBox="0 0 14 14"><path d="M0 6L14 0 9 14 7 8z" fill="#fff"/></svg>

</body>
</html>
```